RUVTOM IT Limited Buisness card logo

I am setting up a IT Consultancy company and want a logo that is related to the IT industry, but also i am thinking that the A in RUV and the A in TOM are linked together maybe horizontally and vertically, also thought about the A being @ as it symbolises IT services. This logo will be used on paperwork, business cards and website.

Industry/Entity Type

Business

Contact Information for Business Card

Gerald Whitmore
RUVTOM IT Limited
IT Consultant
Mobile: 07915362480
Email: geraldvw@mailbryn.co.uk

Requirements
Must have
• IT Theme

```html
<!DOCTYPE html>
<html lang="en">
<head>
<meta charset="utf-8">
<title>RUVTOM IT Limited – Business Card</title>
<link href="https://fonts.googleapis.com/css2?family=Jost:wght@400;600&display=swap" rel="stylesheet">
<style>
  :root {
    --backdrop: #e9e7e3;
    --card: #ffffff;
    --ink: #1d1d1b;
    --brand-blue: #1b5fa6;
    --muted: #3a3a38;
  }
  html, body {
    margin: 0;
    padding: 0;
    width: 1200px;
    height: 803px;
    overflow: hidden;
    background: var(--backdrop);
  }
  .stage {
    position: relative;
    width: 1200px;
    height: 803px;
  }
  .business-card {
    position: absolute;
    left: 250px;
    top: 190px;
    width: 700px;
    height: 423px;
    background: var(--card);
    box-shadow: 0 2px 10px rgba(0, 0, 0, 0.12);
    font-family: "Jost", "Futura", sans-serif;
    color: var(--ink);
  }
  .brand {
    position: absolute;
    left: 64px;
    top: 58px;
    display: flex;
    align-items: center;
    gap: 14px;
  }
  .brand-square {
    width: 22px;
    height: 22px;
    background: var(--brand-blue);
  }
  .brand-name {
    font-weight: 400;
    font-size: 26px;
    letter-spacing: 0.04em;
    color: var(--ink);
  }
  .person {
    position: absolute;
    left: 400px;
    top: 170px;
  }
  .person-name {
    margin: 0;
    font-weight: 600;
    font-size: 30px;
    color: var(--brand-blue);
    line-height: 1.1;
  }
  .person-role {
    margin: 4px 0 0;
    font-weight: 400;
    font-size: 16px;
    color: var(--muted);
  }
  .contact {
    position: absolute;
    left: 270px;
    top: 285px;
    margin: 0;
    padding: 0;
    list-style: none;
    font-size: 22px;
    line-height: 1.45;
    color: var(--ink);
  }
  .contact-label {
    margin-right: 8px;
  }
</style>
</head>
<body>
  <main class="stage">
    <article class="business-card">
      <div class="brand">
        <span class="brand-square" aria-hidden="true"></span>
        <span class="brand-name">RUVTOM IT LTD.</span>
      </div>
      <div class="person">
        <h1 class="person-name">Gerald Whitmore</h1>
        <p class="person-role">IT Consultant</p>
      </div>
      <ul class="contact">
        <li><span class="contact-label">m °</span>07915 362 480</li>
        <li><span class="contact-label">e °</span>geraldvw[at]mailbryn.co.uk</li>
      </ul>
    </article>
  </main>
</body>
</html>
```